Law practice business card

I have an existing logo that I would like to make a little cleaner and maybe something more creative, but using the same base. I would like a contempoary design of the business card.

Industry/Entity Type

Law

Logo Text

On one side of the card - below the logo - I would want to say "TOSPRAVO" and below that it should read "LAW OFFICES, PC" in smaller print. If you have somethign more creative, I would love to see it.

Logo styles of interest
Lettermark Logo
Font styles to use
Sans Serif

Colors

Designer to choose only greyscale colors for use in the design.

Requirements
Must have
• Standard info: My name with "Attorney at Law" underneath; phone, fax, address, email and website.

```html
<!DOCTYPE html>
<html lang="en">
<head>
<meta charset="utf-8">
<title>Tospravo Law Offices – Business Card</title>
<link href="https://fonts.googleapis.com/css2?family=Montserrat:wght@400;600&family=Arimo:wght@400&display=swap" rel="stylesheet">
<style>
  :root {
    --backdrop: #262626;
    --ink: #262626;
    --paper: #ffffff;
    --text: #1a1a1a;
    --muted: #3a3a3a;
    --shadow: rgba(0, 0, 0, 0.35);
  }
  * { margin: 0; padding: 0; box-sizing: border-box; }
  html, body { width: 1200px; height: 1200px; overflow: hidden; }
  body { background: var(--backdrop); position: relative; font-family: "Arimo", Arial, sans-serif; }

  .card { position: absolute; left: 230px; width: 691px; background: var(--paper); overflow: hidden; }
  .card--front { top: 183px; height: 405px; z-index: 2; box-shadow: 0 6px 10px var(--shadow); }
  .card--back { top: 590px; height: 407px; }

  .brand-band { position: absolute; left: 203px; top: 60px; }
  .band-name {
    position: absolute; right: 66px; top: 73px;
    font-family: "Montserrat", sans-serif; font-weight: 600;
    font-size: 21px; letter-spacing: 4px; color: var(--paper);
  }
  .title-rule { position: absolute; left: 228px; right: 0; top: 125px; height: 1.5px; background: var(--ink); }
  .title {
    position: absolute; left: 465px; top: 117px; padding: 0 3px; background: var(--paper);
    font-family: "Montserrat", sans-serif; font-weight: 400; font-size: 12.5px; letter-spacing: 0.5px; color: var(--muted);
  }

  .mark { position: absolute; display: flex; align-items: center; gap: 8px;
    font-family: "Montserrat", sans-serif; font-weight: 600; color: var(--ink); }
  .mark__square { width: 22px; height: 22px; background: var(--ink); }
  .card--front .mark { left: 60px; top: 96px; font-size: 15px; letter-spacing: 2px; }

  .contact { position: absolute; font-size: 13px; color: var(--text); line-height: 22px; }
  .contact--phones { right: 308px; top: 218px; text-align: right; }
  .contact--web { left: 452px; top: 218px; }
  .contact-row { display: flex; align-items: center; gap: 9px; white-space: nowrap; }
  .contact--phones .contact-row { justify-content: flex-end; }
  .contact-row svg { width: 15px; height: 15px; fill: var(--ink); flex: none; }
  .contact-divider { position: absolute; left: 412px; top: 212px; width: 1.5px; height: 52px; background: var(--ink); }
  .contact--address { left: 276px; top: 273px; }

  .logo-lockup { position: absolute; left: 0; right: 0; top: 155px; text-align: center; color: var(--ink); }
  .logo-lockup .mark__square { width: 40px; height: 40px; margin: 0 auto 50px; }
  .logo-lockup__name { font-family: "Montserrat", sans-serif; font-weight: 600; font-size: 24px; letter-spacing: 5px; line-height: 28px; }
  .logo-lockup__sub { font-family: "Montserrat", sans-serif; font-weight: 400; font-size: 9.5px; letter-spacing: 2.5px; margin-top: 2px; color: var(--muted); }
</style>
</head>
<body>

<section class="card card--front" aria-label="Card front">
  <svg class="brand-band" width="488" height="43" viewBox="0 0 488 43" aria-hidden="true">
    <polygon points="0,0 488,0 488,43 42,43" fill="var(--ink)"/>
  </svg>
  <div class="band-name">TOSPRAVO</div>
  <div class="title-rule"></div>
  <div class="title">ATTORNEY AT LAW</div>

  <div class="mark"><span class="mark__square"></span>TOSPRAVO</div>

  <div class="contact contact--phones">
    <div class="contact-row">+34 600 11 22 33
      <svg viewBox="0 0 16 16" aria-label="Phone"><path d="M1 6c0-2 3-3 7-3s7 1 7 3v1h-3V5.5H4V7H1zM4 8h8l2 6H2z"/></svg>
    </div>
    <div class="contact-row">xxx-xxx-xxxx
      <svg viewBox="0 0 16 16" aria-label="Fax"><path d="M4 1h8v5H4zM1 7h14v8H1zm3 3v2h8v-2z"/></svg>
    </div>
  </div>
  <div class="contact-divider"></div>
  <div class="contact contact--web">
    <div class="contact-row">
      <svg viewBox="0 0 16 16" aria-label="Email"><path d="M1 3h14v10H1zm1 1l6 5 6-5z"/></svg>xxxxxx@xxxxx-xxxxxxx
    </div>
    <div class="contact-row">
      <svg viewBox="0 0 16 16" aria-label="Website"><path d="M8 1a7 7 0 100 14A7 7 0 008 1zm0 1.5c1 1 1.7 2.5 1.9 4.5H6.1C6.3 5 7 3.5 8 2.5zM2.6 7h2a10 10 0 01.9-4A5.6 5.6 0 002.6 7zm0 2a5.6 5.6 0 002.9 4 10 10 0 01-.9-4zm3.5 0h3.8C9.7 11 9 12.5 8 13.5 7 12.5 6.3 11 6.1 9zm5.3 0h2a5.6 5.6 0 01-2.9 4 10 10 0 00.9-4zm2-2h-2a10 10 0 00-.9-4 5.6 5.6 0 012.9 4z"/></svg>www.xxxxx-xxxxxxx.com
    </div>
  </div>
  <div class="contact contact--address">
    <div class="contact-row">
      <svg viewBox="0 0 16 16" aria-label="Address" style="height:20px"><path d="M8 0a5.5 5.5 0 00-5.5 5.5C2.5 10 8 16 8 16s5.5-6 5.5-10.5A5.5 5.5 0 008 0zm0 7.5a2 2 0 110-4 2 2 0 010 4z"/></svg>xxxxx xxxxxxx xx-xx xx xxx xxxxxxxx, xxxxxxx
    </div>
  </div>
</section>

<section class="card card--back" aria-label="Card back">
  <div class="logo-lockup">
    <div class="mark__square"></div>
    <div class="logo-lockup__name">TOSPRAVO</div>
    <div class="logo-lockup__sub">LAW OFFICES, PC</div>
  </div>
</section>

</body>
</html>
```